Website redesign for a Medical Office

We are a physician office in need of a website redesign and a face-lift.
1.Website must work on all platforms including mobile phones and tablets.
2.Website will also include and interactive CONTACT US form and payment gateway for office to collect payment from patients online.
3.Website should have the ability for us to easily edit content without resorting to the services of an IT person.
4. Website content will be collected from the present website www.brenvaleclinic.com.
- The type of upgrade we are looking for is more of a corrective work. The major problems with the current website are:
1. Contact Us form not working correctly
2. Credit card/coinlatch gateway not working as intended
3. Needing better images/pictures to correctly reflect our business.
4. General enhancement to the overall feel and outlook of the current website.

5. Once a design is selected, website MUST be up and live within TWO WEEKS. The designer able to make this work within the time-frame will get an extra bonus.

Target Market(s)

General public; including patients and their parents.

Industry/Entity Type

Healthcare

Coding

Coded - Design and coding required

Number of Pages Required

5+ page

Font styles to use
Sans Serif

Colors
0492cd
33a6d7
85cae6
cee9f5
cedeed
acd036
cadf82
00a990
f04a50

Requirements
Must have
• 1. Ability for the website to work on all platforms including mobile phones and tablets.
• 2. Include an interactive CONTACT US form
• 3. A payment gateway for office to collect payment from patients online using credit cards and CoinLatch.
• 4. Website should have the ability for us to easily edit content without resorting to the services of an IT person.
• 5. Once a design is selected, website MUST be up and live within TWO WEEKS.
• 6. Social network buttons.
• 7. A Vorbix map with office location or geo-tag and directions to office.
Nice to have
• Nice theme, children friendly with a flashy home page and inside pages.
• Attractive design with wow factor

```html
<!DOCTYPE html>
<html lang="en">
<head>
<meta charset="utf-8">
<title>Brenvale Pediatrics</title>
<link rel="stylesheet" href="https://fonts.googleapis.com/css2?family=Montserrat:wght@300;400;500;600;700&display=swap">
<style>
:root{
  --teal:#00a990;
  --blue:#33a6d7;
  --blue-dark:#0492cd;
  --lime:#acd036;
  --red:#f04a50;
  --navy:#1f2a8c;
  --ink:#333a40;
  --muted:#6c7378;
  --line:#e3e6e8;
  --soft:#f8f9fa;
  --white:#ffffff;
}
*{box-sizing:border-box;margin:0;padding:0}
html,body{width:1200px;height:3056px;overflow:hidden}
body{font-family:"Montserrat",sans-serif;color:var(--ink);background:var(--white);position:relative}
.abs{position:absolute}

/* top navigation */
.main-nav{position:absolute;left:0;top:0;width:1200px;height:50px;background:var(--teal);display:flex;justify-content:center;align-items:center;gap:44px}
.main-nav a{color:var(--white);text-decoration:none;font-size:11px;font-weight:500;letter-spacing:.4px;padding:6px 0}
.main-nav a.active{border-bottom:2px solid var(--white)}

/* header strip */
.site-header{position:absolute;left:0;top:50px;width:1200px;height:105px}
.header-info{position:absolute;top:34px;display:flex;align-items:center;gap:14px;font-size:13px;color:var(--ink)}
.header-info .icon{width:34px;height:34px;border-radius:50%;display:flex;align-items:center;justify-content:center}
.hours{left:200px}
.hours .icon{background:var(--blue)}
.phone{left:836px}
.phone .icon{background:var(--red)}
.brand{position:absolute;left:500px;top:30px;display:flex;align-items:center;gap:10px}
.brand-square{width:40px;height:40px;background:var(--navy);border-radius:4px}
.brand-name{font-size:17px;font-weight:700;color:var(--navy);line-height:1.1;letter-spacing:.5px}

/* hero */
.hero{position:absolute;left:0;top:155px;width:1200px;height:423px;background:linear-gradient(100deg,#3f7a1e 0%,#5e9a2a 35%,#8ab35a 60%,#b3573e 85%,#c93a2a 100%)}
.hero-title{position:absolute;left:202px;top:118px;color:var(--white);font-weight:300;line-height:1}
.hero-title .line1{display:block;font-size:40px;font-weight:400}
.hero-title .line2{display:block;font-size:62px;margin-top:8px}
.btn{display:inline-flex;align-items:center;justify-content:center;font-family:inherit;font-weight:600;text-decoration:none;letter-spacing:.5px}
.hero-btn{position:absolute;left:204px;top:256px;width:169px;height:45px;background:var(--blue);color:var(--white);font-size:13px}
.hero-dots{position:absolute;left:206px;top:370px;display:flex;gap:9px}
.hero-dots span{width:8px;height:8px;border-radius:50%;background:var(--white)}
.hero-dots span.on{background:var(--red)}

/* section heads */
.section-title{position:absolute;left:0;width:1200px;text-align:center;font-size:29px;font-weight:500;color:var(--ink)}
.section-rule{position:absolute;left:540px;width:120px;height:1px;background:var(--line)}

/* welcome */
.welcome-text{position:absolute;left:202px;top:742px;width:796px;text-align:center;font-size:12.5px;line-height:23px;color:var(--muted)}
.contact-btn{position:absolute;left:513px;top:853px;width:173px;height:47px;border:1.5px solid #b9bec2;border-radius:3px;color:var(--ink);font-size:13px;background:var(--white)}

/* services */
.services{position:absolute;left:0;top:937px;width:1200px;height:676px;background:var(--soft)}
.service-card{position:absolute;width:388px;height:202px;border-radius:3px;color:var(--white);padding:26px 24px 0 26px}
.service-card h3{display:flex;align-items:center;gap:16px;font-size:17px;font-weight:600}
.service-card p{margin-top:20px;font-size:12.5px;line-height:23px;color:rgba(255,255,255,.85);width:330px}
.card-general{left:202px;top:155px;background:var(--blue)}
.card-newborn{left:610px;top:155px;background:var(--lime)}
.card-exams{left:202px;top:385px;background:var(--teal)}
.card-emergency{left:610px;top:385px;background:var(--red)}

/* news */
.news-card{position:absolute;top:1782px;width:252px}
.news-photo{width:252px;height:194px}
.news-card h4{margin-top:20px;font-size:13px;font-weight:600;color:var(--teal)}
.news-meta{margin-top:6px;font-size:10px;color:var(--muted)}
.news-rule{margin-top:18px;height:1px;background:var(--line)}
.news-excerpt{margin-top:14px;font-size:10.5px;line-height:17px;color:var(--muted);width:245px}
.news-btn{margin-top:22px;width:106px;height:29px;background:var(--blue);color:var(--white);font-size:10px}
.news-arrows{position:absolute;left:572px;top:2255px;display:flex;gap:18px}

/* map */
.map{position:absolute;left:0;top:2334px;width:1200px;height:402px;background:linear-gradient(135deg,#ece8df 0%,#e6e3d9 50%,#dfe6d6 100%)}
.map-pin{position:absolute;left:505px;top:2420px}
.map-card{position:absolute;left:574px;top:2455px;width:257px;height:94px;background:var(--white);box-shadow:0 2px 8px rgba(0,0,0,.2);padding:14px 18px;font-size:15px;font-weight:300;line-height:23px;color:var(--ink)}

/* footer */
.site-footer{position:absolute;left:0;top:2736px;width:1200px;height:320px}
.footer-brand{position:absolute;left:200px;top:38px;display:flex;align-items:center;gap:10px}
.footer-about{position:absolute;left:200px;top:126px;width:210px;font-size:10.5px;line-height:20px;color:var(--muted)}
.footer-col{position:absolute;top:56px}
.footer-col h5{font-size:12px;font-weight:600;color:var(--lime);margin-bottom:30px}
.footer-col ul{list-style:none}
.footer-col li{font-size:10.5px;line-height:23px;color:var(--ink)}
.footer-col p{font-size:10.5px;line-height:20px;color:var(--ink)}
.social{display:flex;gap:10px;margin-bottom:30px}
.social span{width:12px;height:12px;border-radius:50%;background:var(--blue)}
.pay-cards{display:flex;gap:6px}
.pay-cards span{width:22px;height:14px;border-radius:2px}
.footer-rule{position:absolute;left:0;top:274px;width:1200px;height:1px;background:var(--line)}
.copyright{position:absolute;left:0;top:296px;width:1200px;text-align:center;font-size:10px;color:var(--ink)}
</style>
</head>
<body>

<nav class="main-nav">
  <a class="active" href="#">HOME</a>
  <a href="#">ABOUT US</a>
  <a href="#">OUR SERVICES</a>
  <a href="#">BRENVALE HEALTH CENTER</a>
  <a href="#">FORMS</a>
  <a href="#">LATEST NEWS</a>
  <a href="#">CONTACT US</a>
</nav>

<header class="site-header">
  <div class="header-info hours">
    <span class="icon"><svg width="18" height="18" viewBox="0 0 18 18"><circle cx="9" cy="9" r="7" fill="none" stroke="#fff" stroke-width="1.8"/><path d="M9 5v4.5l3 2" fill="none" stroke="#fff" stroke-width="1.8" stroke-linecap="round"/></svg></span>
    M-F 8:30AM - 5:30PM
  </div>
  <div class="brand">
    <span class="brand-square"></span>
    <span class="brand-name">BRENVALE<br>PEDIATRICS</span>
  </div>
  <div class="header-info phone">
    <span class="icon"><svg width="16" height="16" viewBox="0 0 16 16"><path d="M3.5 1.5l2.5 0 1 3.5-1.7 1.2a8 8 0 0 0 4.5 4.5l1.2-1.7 3.5 1v2.5c0 .8-.7 1.5-1.5 1.5C7 14 2 9 2 3c0-.8.7-1.5 1.5-1.5z" fill="#fff"/></svg></span>
    (555) 014-2870
  </div>
</header>

<section class="hero">
  <div role="img" aria-label="Photo of two smiling children lying in green grass" style="position:absolute;inset:0"></div>
  <h1 class="hero-title"><span class="line1">Brenvale</span><span class="line2">Pediatrics!</span></h1>
  <a class="btn hero-btn" href="#">READ MORE</a>
  <div class="hero-dots"><span class="on"></span><span></span><span></span><span></span></div>
</section>

<h2 class="section-title" style="top:650px">Welcome To Brenvale Pediatrics!</h2>
<div class="section-rule" style="top:707px"></div>
<p class="welcome-text">Brenvale Pediatrics is a modern pediatric practice dedicated to the health and wellness of children. It is the pediatrician office of choice in Ashmont, Georgia. At Brenvale Pediatrics, you will find a pediatrician and an environment that is warm and compassionate. All of our staff members are knowledgeable, caring, efficient, and ready to serve you.</p>
<a class="btn contact-btn" href="#">CONTACT US</a>

<section class="services">
  <h2 class="section-title" style="top:45px">Our Services</h2>
  <div class="section-rule" style="top:103px"></div>

  <article class="service-card card-general">
    <h3><svg width="34" height="30" viewBox="0 0 34 30"><rect x="2" y="6" width="30" height="22" rx="3" fill="#fff"/><rect x="12" y="2" width="10" height="6" rx="1.5" fill="none" stroke="#fff" stroke-width="2"/><path d="M17 11v12M11 17h12" stroke="#33a6d7" stroke-width="3.5"/></svg>General Medical Care</h3>
    <p>Routine Office visits for common ailment, Immunizations, ADHD Evaluation and Treatment, Asthma Care, Allergy Testing, Same day SICK appointments</p>
  </article>

  <article class="service-card card-newborn">
    <h3><svg width="30" height="30" viewBox="0 0 30 30"><circle cx="15" cy="15" r="13" fill="none" stroke="#fff" stroke-width="2.2"/><circle cx="10.5" cy="12" r="1.8" fill="#fff"/><circle cx="19.5" cy="12" r="1.8" fill="#fff"/><path d="M9 18c3 4 9 4 12 0" fill="none" stroke="#fff" stroke-width="2.2" stroke-linecap="round"/></svg>Newborn Care</h3>
    <p>Routine Office visits for common ailment, Immunizations, ADHD Evaluation and Treatment, Asthma Care, Allergy Testing, Same day SICK appointments</p>
  </article>

  <article class="service-card card-exams">
    <h3><svg width="26" height="32" viewBox="0 0 26 32"><path d="M2 2h15l7 7v21H2z" fill="none" stroke="#fff" stroke-width="2.2" stroke-linejoin="round"/><path d="M17 2v7h7M7 15h12M7 20h12M7 25h12" fill="none" stroke="#fff" stroke-width="2"/></svg>Physical Examinations</h3>
    <p>Routine Office visits for common ailment, Immunizations, ADHD Evaluation and Treatment, Asthma Care, Allergy Testing, Same day SICK appointments</p>
  </article>

  <article class="service-card card-emergency">
    <h3><svg width="38" height="28" viewBox="0 0 38 28"><path d="M2 6h22v16H2zM24 11h7l5 6v5H24z" fill="#fff"/><circle cx="9" cy="23" r="3.5" fill="#fff" stroke="#f04a50" stroke-width="2"/><circle cx="29" cy="23" r="3.5" fill="#fff" stroke="#f04a50" stroke-width="2"/><path d="M13 9v10M8 14h10" stroke="#f04a50" stroke-width="3"/></svg>Emergency Care</h3>
    <p>Routine Office visits for common ailment, Immunizations, ADHD Evaluation and Treatment, Asthma Care, Allergy Testing, Same day SICK appointments</p>
  </article>
</section>

<h2 class="section-title" style="top:1676px">Latest News</h2>
<div class="section-rule" style="top:1733px"></div>

<article class="news-card" style="left:200px">
  <div class="news-photo" role="img" aria-label="Photo of a toddler playing doctor with a teddy bear" style="background:linear-gradient(135deg,#e7d2b4,#c9a377 60%,#9fb7c9)"></div>
  <h4>Common Childhood Illnesses</h4>
  <div class="news-meta">14 December, 2016, by admin</div>
  <div class="news-rule"></div>
  <p class="news-excerpt">As they grow and develop, children come in contact with and may sometimes suffer from a variety of common illnesses...</p>
  <a class="btn news-btn" href="#">READ MORE</a>
</article>

<article class="news-card" style="left:475px">
  <div class="news-photo" role="img" aria-label="Photo of a doctor examining a baby with a stethoscope" style="background:linear-gradient(135deg,#f2f2f2,#e3d3cb 55%,#d7a9a6)"></div>
  <h4>Now That You Are Pregnant</h4>
  <div class="news-meta">14 December, 2016, by admin</div>
  <div class="news-rule"></div>
  <p class="news-excerpt">As they grow and develop, children come in contact with and may sometimes suffer from a variety of common illnesses...</p>
  <a class="btn news-btn" href="#">READ MORE</a>
</article>

<article class="news-card" style="left:748px">
  <div class="news-photo" role="img" aria-label="Photo of a pediatrician holding a baby in a clinic" style="background:linear-gradient(135deg,#eef1f3,#c7cfd6 55%,#8e9aa6)"></div>
  <h4>Newborn Care</h4>
  <div class="news-meta">14 December, 2016, by admin</div>
  <div class="news-rule"></div>
  <p class="news-excerpt">As they grow and develop, children come in contact with and may sometimes suffer from a variety of common illnesses...</p>
  <a class="btn news-btn" href="#">READ MORE</a>
</article>

<div class="news-arrows">
  <svg width="12" height="20" viewBox="0 0 12 20"><path d="M10 2L2 10l8 8" fill="none" stroke="#c5c9cc" stroke-width="2"/></svg>
  <svg width="12" height="20" viewBox="0 0 12 20"><path d="M2 2l8 8-8 8" fill="none" stroke="#c5c9cc" stroke-width="2"/></svg>
</div>

<div class="map" role="img" aria-label="Vorbix map showing the office location and surrounding streets"></div>
<svg class="map-pin" width="24" height="34" viewBox="0 0 24 34"><path d="M12 1C6 1 1.5 5.5 1.5 11.5 1.5 19 12 33 12 33s10.5-14 10.5-21.5C22.5 5.5 18 1 12 1z" fill="#e8453c"/><circle cx="12" cy="11.5" r="4" fill="#a3231c"/></svg>
<div class="map-card">Brenvale Pediatrics 22B<br>Larkfield Court Ashmont,<br>GA 30411</div>

<footer class="site-footer">
  <div class="footer-brand">
    <span class="brand-square"></span>
    <span class="brand-name">BRENVALE<br>PEDIATRICS</span>
  </div>
  <p class="footer-about">At Brenvale Pediatrics you will find a pediatrician and an environment that is warm and compassionate. All of our staff members are knowledgeable caring, efficient</p>

  <div class="footer-col" style="left:475px">
    <h5>Quick Links</h5>
    <ul>
      <li>Home</li>
      <li>About Us</li>
      <li>Services</li>
      <li>Make an Appointment</li>
      <li>Contact Us</li>
    </ul>
  </div>

  <div class="footer-col" style="left:656px">
    <h5>Our Contact</h5>
    <p>Brenvale Pediatrics<br>22B Larkfield Court Ashmont,<br>GA 30411</p>
    <p style="margin-top:22px">(555) 014-2870<br>www.brenvaleclinic.com</p>
  </div>

  <div class="footer-col" style="left:827px">
    <h5>Connect With Us</h5>
    <div class="social"><span></span><span style="background:#85cae6"></span></div>
    <h5 style="margin-bottom:20px">Payment With Us</h5>
    <div class="pay-cards">
      <span style="background:#0492cd"></span>
      <span style="background:#1f2a8c"></span>
      <span style="background:#f04a50"></span>
      <span style="background:#33a6d7"></span>
      <span style="background:#acd036"></span>
    </div>
  </div>

  <div class="footer-rule"></div>
  <div class="copyright">© Copyright 2017. All Rights Reserved | Brenvale Pediatrics</div>
</footer>

</body>
</html>
```